Alterations to existing business card

Here is my current logo and I want the "cafe and bar" taken off with just the words Lumo and our slogan "Ease the craving" on the card, Plus the logo.
Our Current Business Card is currently 5.5cm by 5.5cm and would like it to remain like this thanks.
The loyalty card can be 10 squares with the logo specifying the 10th coffee free. I would like the cheapest option please.
Also on our business card would like the Facebook logo and instagram Logo with TEAHOUSELUMO27 as link to our photos on instagram.

Keep Colour schemes the same please.

On the business cards

Dale Hartwig Director
0427913608
dale27lumo@examplemail.com

Rosa Delacourt Principal
0428150973
roslumo@examplemail.com

Thanks Dale

```html
<!DOCTYPE html>
<html lang="en">
<head>
<meta charset="utf-8">
<title>Lumo – Business and Loyalty Card</title>
<link rel="stylesheet" href="https://fonts.googleapis.com/css2?family=Josefin+Sans:ital,wght@0,300;0,400;1,300&family=Roboto:ital,wght@0,400;1,400&display=swap">
<style>
  :root {
    --backdrop: #b1b1b1;
    --card-dark: #232323;
    --card-light: #f3f3f1;
    --gold: #e2b12c;
    --gold-deep: #c8921a;
    --ink: #1b1b1b;
    --paper-ink: #ffffff;
    --watermark: #e6e6e3;
  }
  * { margin: 0; padding: 0; box-sizing: border-box; }
  html, body { width: 1200px; height: 923px; overflow: hidden; }
  body { background: var(--backdrop); position: relative; font-family: "Roboto", sans-serif; }

  .card { position: absolute; top: 241px; width: 440px; height: 440px; overflow: hidden; }
  .card--loyalty { left: 139px; background: var(--card-dark); }
  .card--contact { left: 619px; background: var(--card-light); }

  /* Loyalty side */
  .brand-mark { position: absolute; border-radius: 50%; border: 3px solid var(--gold); }
  .card--loyalty .brand-mark { left: 73px; top: 48px; width: 106px; height: 106px; }
  .brand-name {
    position: absolute; font-family: "Josefin Sans", sans-serif; font-weight: 300;
    color: var(--paper-ink); letter-spacing: 2px; line-height: 1; text-transform: uppercase;
  }
  .card--loyalty .brand-name { left: 196px; top: 72px; font-size: 60px; }
  .slogan {
    position: absolute; font-family: "Josefin Sans", sans-serif; font-weight: 300; font-style: italic;
    color: var(--gold); font-size: 14px; letter-spacing: 2px; text-transform: uppercase; white-space: nowrap;
  }
  .card--loyalty .slogan { left: 198px; top: 132px; }

  .stamp-grid {
    position: absolute; left: 51px; top: 202px;
    display: grid; grid-template-columns: repeat(5, 48px); grid-auto-rows: 48px;
    column-gap: 24px; row-gap: 24px;
  }
  .stamp { border: 1px solid var(--gold-deep); }

  .social { position: absolute; left: 143px; top: 370px; display: flex; align-items: center; gap: 8px; }
  .social__label { color: var(--paper-ink); font-size: 16px; margin-right: 4px; }
  .social__icon { width: 26px; height: 26px; border-radius: 4px; background: var(--gold); }

  /* Contact side */
  .watermark {
    position: absolute; left: 60px; top: 55px; width: 326px; height: 326px;
    border-radius: 50%; border: 6px solid var(--watermark);
  }
  .vertical {
    position: absolute; writing-mode: vertical-rl; transform: rotate(180deg); white-space: nowrap;
  }
  .card--contact .brand-name {
    color: var(--ink); font-size: 58px; left: 62px; top: 70px; font-weight: 400;
  }
  .card--contact .slogan { left: 114px; top: 72px; font-size: 14px; }
  .card--contact .brand-mark { left: 49px; top: 265px; width: 98px; height: 98px; }

  .person { position: absolute; left: 198px; color: var(--ink); }
  .person--director { top: 70px; }
  .person--principal { top: 251px; }
  .person__name { font-family: "Josefin Sans", sans-serif; font-weight: 300; font-size: 30px; line-height: 1.1; }
  .person__role { font-style: italic; font-size: 16px; margin-top: 6px; }
  .person__details { margin-top: 20px; font-size: 16px; line-height: 23px; }
</style>
</head>
<body>
  <section class="card card--loyalty">
    <div class="brand-mark"></div>
    <div class="brand-name">Lumo</div>
    <div class="slogan">Ease the craving</div>
    <div class="stamp-grid">
      <div class="stamp"></div><div class="stamp"></div><div class="stamp"></div><div class="stamp"></div><div class="stamp"></div>
      <div class="stamp"></div><div class="stamp"></div><div class="stamp"></div><div class="stamp"></div><div class="stamp"></div>
    </div>
    <div class="social">
      <span class="social__label">Follows On</span>
      <span class="social__icon" role="img" aria-label="Social link"></span>
      <span class="social__icon" role="img" aria-label="Photo page link"></span>
    </div>
  </section>

  <section class="card card--contact">
    <div class="watermark"></div>
    <div class="vertical brand-name">Lumo</div>
    <div class="vertical slogan">Ease the craving</div>
    <div class="brand-mark"></div>

    <div class="person person--director">
      <div class="person__name">Dale Hartwig</div>
      <div class="person__role">Director</div>
      <div class="person__details">0427913608<br>dale27lumo@examplemail.com</div>
    </div>
    <div class="person person--principal">
      <div class="person__name">Rosa Delacourt</div>
      <div class="person__role">Principal</div>
      <div class="person__details">0428150973<br>roslumo@examplemail.com</div>
    </div>
  </section>
</body>
</html>
```